Business Card/ Email Signature Design Project

I am an Interior Designer. I need a business card that looks sophisticated stylish but simple in design. My work covers space design/ interior architecture/ furniture design/ product development & styling.

I have a very specific brief and know mostly what I want. I'm hoping to work with someone who can translate my ideas.

My branding should have a strong focus on my name, the majority of my work is referral based.
I'm keen to keep a monochromatic colour scheme: dark charcoal/ black/ white/ embossing/ silver. I'm not suggesting we use all that I've listed, they are possible ideas at this stage. I will need to be mindful of printing costs an also how I make the design work across, cards, letter heads, email logo and web design.

Theory behind images sent below;
1-Rug Image_(minus boarder) I was thinking this image could be used on the back of the card with my contact details over. I like that the lines are almost hand drawn and start to look free form. It's a subtle contrast to a more formal front of the card with my name.
2_Tomas Ferle_I really like the orientation, the proportion of font on the card, the colour and the font. I like the lower case for my name and the upper case for 'Interior Design'. Not sure if it should be 'Interior Designer or Interior Design' at this stage, was leaning towards 'Interior Design'. Was thinking the 'i' and 'd' in my surname could be the colour eg 'silver'?? We can decide on this once we see it.

Look forward to hearing from you.
Cheers,
Saskia Bremond

Printing

Saskia Bremond Interior Design

```html
<!DOCTYPE html>
<html lang="en">
<head>
<meta charset="utf-8">
<title>Saskia Bremond Interior Design — Business Card</title>
<link rel="stylesheet" href="https://fonts.googleapis.com/css2?family=Montserrat:wght@300;400;600&display=swap">
<style>
  :root {
    --backdrop: #2a2a2a;
    --card-black: #0f0f0f;
    --card-edge: #1c1c1c;
    --foil-silver: #c9c9c9;
    --name-silver: #8e8e8e;
    --tagline-grey: #5a5a5a;
    --pattern-dark: #161616;
    --pattern-light: #3a3a3a;
  }
  * { margin: 0; padding: 0; box-sizing: border-box; }
  html, body {
    width: 1200px;
    height: 900px;
    overflow: hidden;
    background: var(--backdrop);
    font-family: "Montserrat", Arial, sans-serif;
  }
  .canvas {
    position: relative;
    width: 1200px;
    height: 900px;
    display: flex;
    align-items: center;
    justify-content: center;
    gap: 40px;
  }
  .card {
    position: relative;
    width: 525px;
    height: 300px;
    background: var(--card-black);
    border: 1px solid var(--card-edge);
    overflow: hidden;
  }
  .card-back .rug-pattern {
    position: absolute;
    inset: 0;
    background: radial-gradient(ellipse at 75% 30%, var(--pattern-light) 0%, var(--pattern-dark) 55%, var(--card-black) 100%);
  }
  .contact-list {
    position: absolute;
    left: 200px;
    top: 110px;
    list-style: none;
    color: var(--foil-silver);
    font-size: 12.5px;
    font-weight: 400;
    line-height: 1.45;
  }
  .contact-list .label { display: inline-block; width: 20px; }
  .card-front {
    display: flex;
    flex-direction: column;
    justify-content: center;
    padding-left: 52px;
  }
  .brand-name {
    color: var(--name-silver);
    font-size: 54px;
    font-weight: 600;
    letter-spacing: 0.5px;
    line-height: 1;
  }
  .brand-tagline {
    margin-top: 6px;
    color: var(--tagline-grey);
    font-size: 21px;
    font-weight: 300;
    letter-spacing: 9.5px;
    text-transform: uppercase;
  }
</style>
</head>
<body>
  <main class="canvas">
    <section class="card card-back">
      <div class="rug-pattern" role="img" aria-label="Hand-drawn free-form crackle line pattern in silver foil on black"></div>
      <ul class="contact-list">
        <li><span class="label">A:</span>P.O Box 214 Northcote VIC. 3070</li>
        <li><span class="label">M:</span>0400 555 172</li>
        <li><span class="label">E:</span>interiors@saskiabremond.com</li>
        <li><span class="label">W:</span>www.saskiabremond.com</li>
      </ul>
    </section>
    <section class="card card-front">
      <h1 class="brand-name">saskia bremond</h1>
      <p class="brand-tagline">Interior Design</p>
    </section>
  </main>
</body>
</html>
```